Migration and redesign of existing website to WordPress using DIVI 3

I. TASK OBJECTIVE:
- Redesign our existing website www.calderwynhealth.com.au with a fresh new look and migrate to new Wordpress site based on DIVI3 theme. The site will contain the same basic functionality as the existing site (with some small changes).

II. STYLE/ DESIGN ASPECT:
As an example of a site that I like the look of, see https://tanglorix.com/. I like the use of shadows, and this would go well with the little animations you can do with Divi (e.g. when hovering over pics).

1. What I am looking for is a design which has lots of white space, is modern and friendly looking (but still not too cute or frivolous, as we are a medical practice)
2. DESIGN that is NOT TOO rectangular or blocky.
3. Please take into consideration our Users are Older market, so any icons or navigation features need to be very easy to understand and not too small.
4. Must be easy to navigate
5. We are are happy to go with a new colour scheme, and are working on some ideas for this, but happy to take suggestions.

III. SPECIFICATIONS:
1. 5+ Pages (should flow like the current site)
2. Using Wordpress Divi 3 theme.
3. I'd like every page to have a "book now" button and a contact form in a sidebar so that users can click the button or fill in the contact form without scrolling at all. EXCEPT ON THE HOME PAGE, where there should still be a book now button (maybe on the top right in the header of all pages?), and maybe a contact us button which scrolls down to the contact area at the bottom of the HOME page. I don't think a side bar is necessarily required on the home page, but if you think it makes sense from a design perspective please let me know.
4. AT THE BOTTOM OF THE PAGE, just above the FOOTER, I'd like a row of trust logos for various organisations that we are affiliated with. (A list of this company will be provided later but you could temporarily use placeholders)

Once we have a structure in place, we can migrate most of the content. Please let me know if I'm not being clear or you need further information.

Target Market(s)

Podiatry Customers and Referrors

Industry/Entity Type

Health Care

Coding

Coded - Design and coding required

Number of Pages Required

5+ page

Colors

Designer to choose colors to be used in the design.

Requirements
Must have
• Simple to navigate.
• Contact/booking details on most if not all pages - please see specification above
• Section for Trusted Affiliates above the footer
• Wordpress using Divi3 Theme
Nice to have
• Not too busy with the design. Plenty of white space or light background.
Should not have
• Should not be complicated to navigate.
• TOO rectangular or blocky designs

```html
<!DOCTYPE html>
<html lang="en">
<head>
<meta charset="utf-8">
<title>Calderwyn Foot Health</title>
<link href="https://fonts.googleapis.com/css2?family=Poppins:wght@300;400;500;600&family=Oswald:wght@400;500&display=swap" rel="stylesheet">
<style>
:root{
  --blue:#1b93c6;
  --blue-deep:#0f6f96;
  --navy:#0d5676;
  --ink:#2b2f33;
  --text:#5d6368;
  --topbar:#2f3437;
  --orange:#f6931e;
  --mist:#f2f5f7;
  --white:#ffffff;
}
*{box-sizing:border-box;margin:0;padding:0}
html,body{width:1200px;height:4724px;overflow:hidden}
body{position:relative;font-family:"Poppins",sans-serif;color:var(--text);background:var(--white)}
.abs{position:absolute}
.btn{display:inline-block;border-radius:20px;background:var(--blue);color:#fff;font-size:12px;font-weight:600;letter-spacing:.5px;padding:8px 20px;text-transform:uppercase}

/* top bar + header */
.topbar{left:0;top:0;width:1200px;height:38px;background:var(--topbar)}
.topbar .phone{left:640px;top:7px;color:#fff;font-size:12px;line-height:12px;display:flex;gap:8px;align-items:center}
.topbar .phone small{display:block;font-size:8px;color:#bbb}
.topbar .book{left:800px;top:0;width:135px;height:38px;background:var(--blue);color:#fff;text-align:center;font-size:14px;font-weight:600;line-height:18px;padding-top:3px}
.topbar .book small{display:block;font-size:7px;font-weight:400}
.topbar .social{left:1040px;top:11px;display:flex;gap:14px}
.topbar .social span{width:16px;height:16px;border-radius:50%;background:#fff;opacity:.85}
.header{left:0;top:38px;width:1200px;height:100px;background:rgba(255,255,255,.9)}
.brand{left:95px;top:60px;display:flex;align-items:center;gap:10px;color:var(--blue-deep);font-size:19px;font-weight:500}
.brand .dot{width:32px;height:32px;border-radius:50%;background:var(--blue)}
.nav{left:400px;top:78px;display:flex;gap:30px;font-size:12px;font-weight:500;color:var(--ink)}
.nav .active{color:var(--blue);border-bottom:2px solid var(--blue);padding-bottom:6px}

/* hero */
.hero-photo{left:0;top:138px;width:1200px;height:640px;background:linear-gradient(110deg,#c9d6df 0%,#e8eef2 40%,#d7c9b7 70%,#e9e2d8 100%)}
.hero-wave{left:0;top:560px}
.hero-bubble{left:126px;top:236px;width:380px;height:270px;border-radius:50%;background:rgba(27,147,198,.72);box-shadow:0 10px 30px rgba(0,0,0,.2);text-align:center;color:#fff;padding-top:58px}
.hero-bubble h1{font-family:"Oswald",sans-serif;font-weight:400;font-size:25px;line-height:38px;letter-spacing:.5px}
.hero-bubble .btn{margin-top:16px;background:var(--blue-deep)}

/* services */
.services{left:110px;top:880px;width:980px;display:flex;justify-content:space-between}
.service{width:230px;text-align:center}
.service .ring{width:200px;height:200px;margin:0 auto;border-radius:50%;padding:12px;background:linear-gradient(150deg,#37b4e6,#0f79aa);box-shadow:0 8px 18px rgba(0,0,0,.2)}
.service .ring div{width:100%;height:100%;border-radius:50%;border:4px solid #fff;background:linear-gradient(140deg,#e8d4c4,#c79c86)}
.service h3{margin-top:30px;font-size:14px;font-weight:500;color:var(--ink)}
.service p{margin:8px auto 0;width:190px;font-size:11px;line-height:17px}
.service .btn{margin-top:16px;padding:6px 18px;font-size:10px}

/* divider */
.divider{left:0;top:1290px}
.mark{left:0;top:1490px;width:1200px;text-align:center}
.mark .dot{display:inline-block;width:64px;height:64px;border-radius:50%;background:var(--blue);opacity:.85}
.mark .line{width:140px;height:3px;margin:8px auto 0;background:var(--blue-deep);border-radius:2px}

/* about */
.about{left:113px;top:1630px;width:700px}
.about h2{font-size:38px;font-weight:500;color:var(--ink);margin-bottom:20px}
.about p{font-size:12px;line-height:20px;margin-bottom:10px}
.about .lead{font-size:16px;font-weight:500;color:var(--ink);margin:8px 0 10px}
.about .point{display:flex;gap:6px;align-items:center;color:var(--blue);font-size:13px;font-weight:600;text-transform:uppercase}
.about .point + p{margin-top:2px}
.about .btn{margin-top:10px}
.about a{color:var(--blue)}
.portrait{left:830px;top:1650px;width:260px;height:420px;border-radius:6px;background:linear-gradient(180deg,#f7f7f7 0%,#e8d8c8 60%,#d6b49c 100%)}
.name-tag{left:830px;top:2080px;width:260px;height:52px;background:var(--blue);color:#fff;text-align:center;font-size:14px;font-weight:500;padding-top:7px;line-height:18px}
.name-tag small{display:block;font-size:11px;font-weight:400}

/* free book */
.book-band{left:0;top:2220px;width:1200px;height:670px;background:linear-gradient(90deg,#eef1f3 0%,#f7f8f9 50%,#e6ecf0 100%)}
.book-copy{left:195px;top:2400px;width:520px}
.book-copy h2{font-size:52px;font-weight:400;color:var(--ink);line-height:56px}
.book-copy h3{font-size:19px;font-weight:500;color:var(--ink);line-height:26px}
.book-copy h3 span{color:var(--blue)}
.book-copy p{font-size:13px;line-height:22px;margin-top:24px;width:470px}
.book-copy .btn{margin-top:24px;background:var(--orange)}
.cover{left:778px;top:2310px;width:270px;height:470px;background:#fff;box-shadow:8px 12px 28px rgba(0,0,0,.28);border-left:10px solid #d8dde0}
.cover h4{margin:22px 16px 4px;font-size:22px;font-weight:600;color:var(--navy)}
.cover p{margin:0 16px;font-size:9px;line-height:13px;color:var(--ink)}
.cover .photo{position:absolute;left:0;bottom:0;width:100%;height:270px;background:linear-gradient(160deg,#7fa7b8,#3c6d84 60%,#2a4a5b)}

/* team */
.team-title{left:0;top:2955px;width:1200px;text-align:center;font-size:38px;font-weight:400;color:var(--ink)}
.team{left:113px;top:3050px;width:974px;display:flex;justify-content:space-between}
.member{width:222px;height:283px;position:relative;background:linear-gradient(180deg,#f3f3f3,#e3d3c5);box-shadow:0 6px 14px rgba(0,0,0,.12)}
.member .label{position:absolute;left:0;bottom:0;width:100%;height:54px;background:var(--blue);color:#fff;text-align:center;font-size:14px;font-weight:500;padding-top:8px;line-height:18px}
.member .label small{display:block;font-size:11px;font-weight:400}
.arrow{top:3160px}

/* partners */
.partners-title{left:0;top:3460px;width:1200px;text-align:center;font-size:38px;font-weight:400;color:var(--ink)}
.partners{left:113px;top:3565px;width:974px;display:flex;justify-content:space-between}
.partners span{width:160px;height:38px;border-radius:6px;background:#2a2d30;opacity:.85}

/* footer */
.foot-wave{left:0;top:3640px}
.newsletter{left:113px;top:3845px;display:flex}
.newsletter .field{width:344px;height:50px;background:var(--navy);color:#cfe3ec;font-size:13px;padding:15px 16px}
.newsletter .go{width:126px;height:50px;background:#cfdde3;color:var(--navy);font-size:13px;font-weight:600;text-align:center;padding-top:15px}
.contact{left:113px;top:3935px;color:#fff}
.contact h2{font-size:29px;font-weight:500;margin-bottom:18px}
.contact .row{display:flex;gap:10px;font-size:14px;line-height:22px;margin-bottom:14px}
.foot-brand{left:113px;top:4100px;display:flex;align-items:center;gap:10px;color:#dff1f8;font-size:19px;font-weight:500}
.foot-brand .dot{width:40px;height:40px;border-radius:50%;background:#dff1f8;opacity:.8}
.appoint{left:583px;top:3925px;width:505px;height:340px;background:var(--navy);box-shadow:0 10px 24px rgba(0,0,0,.25);padding:26px 24px}
.appoint h2{color:#fff;font-size:29px;font-weight:400;letter-spacing:.5px;margin-bottom:22px}
.appoint .grid{display:grid;grid-template-columns:1fr 1fr;gap:16px 20px}
.appoint .in{height:38px;background:#fff;font-size:11px;color:var(--ink);padding:11px 10px}
.appoint .area{grid-column:1/3;height:110px}
.submit{left:605px;top:4245px;width:460px;height:42px;background:#0b4a66;color:#fff;text-align:center;font-size:14px;font-weight:600;padding-top:11px}
.map{left:0;top:4250px;width:1200px;height:320px;background:linear-gradient(135deg,#dde6dc 0%,#e4eaee 50%,#cfdfea 100%)}
.bottom{left:0;top:4570px;width:1200px;height:154px;background:var(--navy);text-align:center}
.bottom .social{display:flex;justify-content:center;gap:12px;margin-top:42px}
.bottom .social span{width:26px;height:26px;border-radius:50%;background:#fff}
.bottom p{margin-top:18px;color:#cfe3ec;font-size:11px}
</style>
</head>
<body>

<!-- hero -->
<div class="abs hero-photo" role="img" aria-label="Podiatrist examining a patient's leg in a bright clinic room"></div>
<svg class="abs hero-wave" width="1200" height="230" viewBox="0 0 1200 230" aria-hidden="true">
  <path d="M0 110 C 180 240 330 150 520 170 C 720 190 860 40 1000 60 C 1090 72 1150 110 1200 130 L1200 230 L0 230 Z" fill="#fff"/>
</svg>

<div class="abs topbar">
  <div class="abs phone">
    <svg width="18" height="18" viewBox="0 0 24 24" fill="#fff"><path d="M6.6 10.8a15 15 0 0 0 6.6 6.6l2.2-2.2c.3-.3.7-.4 1-.2 1.1.4 2.3.6 3.6.6.6 0 1 .4 1 1V20c0 .6-.4 1-1 1A17 17 0 0 1 3 4c0-.6.4-1 1-1h3.5c.6 0 1 .4 1 1 0 1.3.2 2.5.6 3.6.1.3 0 .7-.2 1Z"/></svg>
    <div><small>CALL US</small>(08) 5550 2417</div>
  </div>
  <div class="abs book">BOOK NOW<small>ONLINE APPOINTMENT BOOKING</small></div>
  <div class="abs social"><span></span><span></span><span></span><span></span></div>
</div>
<div class="abs header"></div>
<div class="abs brand"><span class="dot"></span>Calderwyn Foot Health</div>
<nav class="abs nav">
  <span class="active">ABOUT US</span><span>COMMON PROBLEMS</span><span>SERVICES</span><span>CASE HISTORIES</span><span>INFORMATION</span><span>BLOG</span><span>CONTACT</span>
</nav>

<div class="abs hero-bubble">
  <h1>WE OFFER TREATMENTS TO<br>ALLEVIATE PAIN AND GET ATHLETES<br>AND DANCERS BACK IN ACTION<br>QUICKLY</h1>
  <span class="btn">Learn More</span>
</div>

<!-- services -->
<section class="abs services">
  <div class="service"><div class="ring"><div role="img" aria-label="Close-up of a painful heel"></div></div><h3>HEEL AND ARCH PAIN</h3><p>When you suffer from a foot and/or ankle problem, the pain and discomfort can make it...</p><span class="btn">Learn More</span></div>
  <div class="service"><div class="ring"><div role="img" aria-label="Foot skin and nail care treatment"></div></div><h3>SKIN AND NAIL CARE</h3><p>When you suffer from a foot and/or ankle problem, the pain and discomfort can make it...</p><span class="btn">Learn More</span></div>
  <div class="service"><div class="ring"><div role="img" aria-label="Athlete holding an injured ankle"></div></div><h3>SPORTS INJURIES</h3><p>When you suffer from a foot and/or ankle problem, the pain and discomfort can make it...</p><span class="btn">Learn More</span></div>
  <div class="service"><div class="ring"><div role="img" aria-label="Bandaged foot after a sports injury"></div></div><h3>SPORTS INJURIES</h3><p>When you suffer from a foot and/or ankle problem, the pain and discomfort can make it...</p><span class="btn">Learn More</span></div>
</section>

<svg class="abs divider" width="1200" height="200" viewBox="0 0 1200 200" aria-hidden="true">
  <path d="M0 90 C 200 20 380 150 600 110 C 820 70 980 0 1200 40 L1200 200 L0 200 Z" fill="#f3f5f7"/>
  <path d="M0 140 C 240 80 420 190 640 150 C 860 110 1000 90 1200 120 L1200 200 L0 200 Z" fill="#fff"/>
</svg>
<div class="abs mark"><span class="dot"></span><div class="line"></div></div>

<!-- about -->
<section class="abs about">
  <h2>ABOUT US</h2>
  <p><a>Calderwyn Foot Health</a> was established in 1991 by Dr Mara Ellison. We currently have six podiatrists and two administrative staff members housed in a modern, state-of-the-art clinic, with simple parking on site.</p>
  <div class="lead">In our offices, we help our patients</div>
  <div class="point"><svg width="14" height="14" viewBox="0 0 16 16"><rect x="1" y="1" width="14" height="14" rx="2" fill="none" stroke="#1b93c6" stroke-width="1.6"/><path d="M4 8l3 3 5-6" fill="none" stroke="#1b93c6" stroke-width="2"/></svg>Regain Control</div>
  <p>Just like you, we want you to get better as soon as possible. That is why we focus on making your visit an informative and supportive experience, empowering you to take control of your condition and make the best possible treatment choice. We even offer specific...</p>
  <div class="point"><svg width="14" height="14" viewBox="0 0 16 16"><rect x="1" y="1" width="14" height="14" rx="2" fill="none" stroke="#1b93c6" stroke-width="1.6"/><path d="M4 8l3 3 5-6" fill="none" stroke="#1b93c6" stroke-width="2"/></svg>Explore All Possible Solutions</div>
  <p>We offer both non-invasive and surgical remedies for most conditions, and have a medical laser in-office for musculoskeletal treatments. We often work with trainers, physical therapists, and other professionals to provide additional intervention and rehabilitation options...</p>
  <div class="point"><svg width="14" height="14" viewBox="0 0 16 16"><rect x="1" y="1" width="14" height="14" rx="2" fill="none" stroke="#1b93c6" stroke-width="1.6"/><path d="M4 8l3 3 5-6" fill="none" stroke="#1b93c6" stroke-width="2"/></svg>Stay Pain-Free For Life</div>
  <p>We build relationships with our patients, keeping them on their feet for as long as they live. Since we remove neuromas, correct sporting injuries, create customised insoles (orthoses) to correct gait and posture, and offer preventive and corrective wound care for adults, we are a one-stop-shop for comprehensive...</p>
  <span class="btn">View More</span>
</section>
<div class="abs portrait" role="img" aria-label="Portrait of the practice's podiatric surgeon"></div>
<div class="abs name-tag">MARA ELLISON<small>Podiatric Surgeon</small></div>

<!-- free book -->
<div class="abs book-band" role="img" aria-label="Faded image of a surgeon's gloved hands"></div>
<section class="abs book-copy">
  <h2>FREE BOOK</h2>
  <h3>Free Foot Surgery Book by Podiatric Surgeon,<br><span>Dr Mara Ellison</span></h3>
  <p>This book was created to demonstrate examples of some foot conditions that can be surgically corrected by our Podiatric Surgeon, Dr Mara Ellison.</p>
  <span class="btn">View Details</span>
</section>
<div class="abs cover">
  <h4>Podiatric Surgery</h4>
  <p>Dr Mara Ellison MSc, BSc, PGradDipHlthSc, FACPS</p>
  <p style="margin-top:14px">Calderwyn Foot Health<br>14 Ferndale Road<br>Kellmoor WA 6099</p>
  <div class="photo" role="img" aria-label="Surgical team in an operating theatre"></div>
</div>

<!-- team -->
<h2 class="abs team-title">OUR TEAM</h2>
<svg class="abs arrow" style="left:78px" width="22" height="44" viewBox="0 0 22 44"><path d="M18 4 L4 22 L18 40" fill="none" stroke="#b9d8e6" stroke-width="2"/></svg>
<svg class="abs arrow" style="left:1100px" width="22" height="44" viewBox="0 0 22 44"><path d="M4 4 L18 22 L4 40" fill="none" stroke="#b9d8e6" stroke-width="2"/></svg>
<section class="abs team">
  <div class="member" role="img" aria-label="Portrait of Mara Ellison"><div class="label">MARA ELLISON<small>Podiatric Surgeon</small></div></div>
  <div class="member" role="img" aria-label="Portrait of Owen Tralley"><div class="label">OWEN TRALLEY<small>Podiatrist</small></div></div>
  <div class="member" role="img" aria-label="Portrait of Priya Danvers"><div class="label">PRIYA DANVERS<small>Podiatrist</small></div></div>
  <div class="member" role="img" aria-label="Portrait of Hallie Brook"><div class="label">HALLIE BROOK<small>Podiatrist</small></div></div>
</section>

<!-- partners -->
<h2 class="abs partners-title">OUR PARTNERS</h2>
<section class="abs partners" aria-label="Affiliated organisations">
  <span></span><span></span><span></span><span></span><span></span>
</section>

<!-- footer -->
<svg class="abs foot-wave" width="1200" height="620" viewBox="0 0 1200 620" aria-hidden="true">
  <path d="M0 60 C 160 0 260 110 420 80 C 620 40 700 150 900 90 C 1040 50 1120 20 1200 30 L1200 620 L0 620 Z" fill="#7cc3e0" opacity=".5"/>
  <path d="M0 100 C 180 40 300 150 480 110 C 680 70 760 170 960 120 C 1080 90 1150 70 1200 80 L1200 620 L0 620 Z" fill="#1b87b8"/>
</svg>
<div class="abs newsletter"><div class="field">Enter Your Email</div><div class="go">SUBSCRIBE</div></div>
<section class="abs contact">
  <h2>CONTACT US</h2>
  <div class="row"><svg width="14" height="20" viewBox="0 0 14 20"><path d="M7 0a7 7 0 0 0-7 7c0 5 7 13 7 13s7-8 7-13a7 7 0 0 0-7-7Zm0 10a3 3 0 1 1 0-6 3 3 0 0 1 0 6Z" fill="#fff"/></svg><div>14 Ferndale Road Kellmoor,<br>WA 6099</div></div>
  <div class="row"><svg width="16" height="16" viewBox="0 0 24 24" fill="#fff"><path d="M6.6 10.8a15 15 0 0 0 6.6 6.6l2.2-2.2c.3-.3.7-.4 1-.2 1.1.4 2.3.6 3.6.6.6 0 1 .4 1 1V20c0 .6-.4 1-1 1A17 17 0 0 1 3 4c0-.6.4-1 1-1h3.5c.6 0 1 .4 1 1 0 1.3.2 2.5.6 3.6.1.3 0 .7-.2 1Z"/></svg><div>Call Us: (08) 5550 2417</div></div>
</section>
<div class="abs foot-brand"><span class="dot"></span>Calderwyn Foot Health</div>

<div class="abs map" role="img" aria-label="Embedded street map showing the clinic location"></div>

<section class="abs appoint">
  <h2>REQUEST AN APPOINTMENT</h2>
  <div class="grid">
    <div class="in">Name:</div><div class="in">Email:</div>
    <div class="in">Contact:</div><div class="in">Subject:</div>
    <div class="in area">Contact:</div>
  </div>
</section>
<div class="abs submit">SUBMIT</div>

<footer class="abs bottom">
  <div class="social"><span></span><span></span><span></span><span></span></div>
  <p>©2017 Calderwyn Foot Health. All Rights Reserved. Reproduced with Permission. Privacy Policy</p>
</footer>

</body>
</html>
```